New Optometry Practice needs a Business Card

Need a business card for an Optometry practice called 'Marlow Family Eyecare'. I would like to use designs that are friendly, fun and professional. Looking to incorporate glasses (see uploaded image). Not interested in design with an 'eye' in logo. Like green, blue, white as color choices..but open to your ideas. Back of card will be an appointment card as well as provide address, phone and email information.

Industry/Entity Type

Business

Contact Information for Business Card

Marlow Family Eyecare
Dr. Celeste Varga, Optometrist (or O.D.)
4170 S Brackenridge Rd Wenatchee, WA 98802
CMarlowfamilyeyecare.example

Colors
acd036
33b8a4
f68d4e
cfeae6
fee18a
cadf82

Requirements
Must have
• Appointment card on back with date/time of return for next exam

```html
<!DOCTYPE html>
<html lang="en">
<head>
<meta charset="utf-8">
<title>Marlow Family Eyecare – Business Card</title>
<link href="https://fonts.googleapis.com/css2?family=Open+Sans:wght@400;600;700&display=swap" rel="stylesheet">
<style>
  :root {
    --bg: #e9ebee;
    --card: #ffffff;
    --navy-blue: #0b72b5;
    --sky-blue: #1ba6de;
    --ink: #1c1c1c;
    --rule: #d9dde2;
  }
  * { box-sizing: border-box; margin: 0; padding: 0; }
  html, body { width: 1200px; height: 1000px; overflow: hidden; }
  body {
    background: var(--bg);
    font-family: "Open Sans", Arial, sans-serif;
    color: var(--ink);
    position: relative;
  }
  .card {
    position: absolute;
    left: 265px;
    width: 665px;
    height: 398px;
    background: var(--card);
    border-radius: 22px;
    overflow: hidden;
  }
  .card--front { top: 73px; }
  .card--back { top: 532px; }

  .band {
    position: absolute;
    left: 0; right: 0;
    display: flex;
    background: var(--card);
  }
  .band__cap { width: 26px; background: var(--sky-blue); }
  .band__main {
    flex: 1;
    margin: 0 4px;
    background: var(--navy-blue);
    color: #fff;
    display: flex;
    align-items: center;
    justify-content: center;
  }

  /* Front */
  .brand-name {
    position: absolute;
    top: 150px; left: 0; right: 0;
    text-align: center;
    font-size: 44px;
    font-weight: 700;
    color: var(--navy-blue);
    letter-spacing: -0.5px;
  }
  .doctor {
    position: absolute;
    top: 246px; left: 0; right: 0;
    text-align: center;
    color: var(--navy-blue);
  }
  .doctor__name { font-size: 22px; font-weight: 700; }
  .doctor__title { font-size: 18px; color: var(--sky-blue); }
  .contacts {
    position: absolute;
    top: 294px; left: 0; right: 0;
    display: flex;
    justify-content: center;
    gap: 20px;
    font-size: 16px;
  }
  .contacts__item { display: flex; align-items: center; gap: 7px; }
  .contacts__item svg { width: 15px; height: 15px; fill: var(--navy-blue); }
  .divider {
    position: absolute;
    top: 323px; left: 80px; right: 80px;
    height: 1px;
    background: var(--rule);
  }
  .website {
    position: absolute;
    top: 328px; left: 0; right: 0;
    text-align: center;
    font-size: 17px;
    letter-spacing: 0.6px;
  }
  .card--front .band { top: 365px; height: 33px; }
  .address { font-size: 17px; letter-spacing: 1.6px; }

  /* Back */
  .card--back .band--top { top: 0; height: 38px; }
  .card--back .band--bottom { bottom: 0; height: 33px; }
  .band__title { font-size: 18px; font-weight: 700; letter-spacing: 0.2px; }
  .field-line {
    position: absolute;
    left: 145px; width: 377px;
    height: 2px;
    background: var(--ink);
  }
  .field-line--for { top: 118px; }
  .field-line--when { top: 257px; }
  .field-label {
    position: absolute;
    font-size: 16px;
  }
  .days {
    position: absolute;
    top: 184px; left: 32px; right: 30px;
    display: flex;
    justify-content: space-between;
    font-size: 16px;
  }
  .day { display: flex; align-items: center; gap: 6px; }
  .day__box {
    width: 24px; height: 16px;
    border: 2px solid var(--navy-blue);
    border-radius: 5px;
  }
  .policy {
    position: absolute;
    top: 312px; left: 0; right: 0;
    text-align: center;
  }
  .policy__title { font-size: 16px; font-weight: 600; color: var(--navy-blue); letter-spacing: 0.3px; }
  .policy__text { font-size: 17px; margin-top: 2px; }
</style>
</head>
<body>

<section class="card card--front">
  <div class="brand-name">Marlow Family Eyecare</div>

  <div class="doctor">
    <span class="doctor__name">Dr. Celeste Varga</span><span class="doctor__title">, Optometrist</span>
  </div>

  <div class="contacts">
    <span class="contacts__item">
      <svg viewBox="0 0 16 16" aria-hidden="true"><path d="M2 6c0-2 2-3 6-3s6 1 6 3v1h-3V5.5H5V7H2zM4 8h8l2 5H2z"/></svg>
      + 000 000 0000
    </span>
    <span class="contacts__item">
      <svg viewBox="0 0 16 16" aria-hidden="true"><path d="M1 3h14v10H1zM2.5 4.5 8 9l5.5-4.5v1L8 10 2.5 5.5z" fill-rule="evenodd"/></svg>
      info@Marlowfamilyeyecare.example
    </span>
    <span class="contacts__item">
      <svg viewBox="0 0 16 16" aria-hidden="true"><path d="M4 1h8v4H4zM1 6h14v6h-3v3H4v-3H1zM5 10v4h6v-4z" fill-rule="evenodd"/></svg>
      + 000 000 0000
    </span>
  </div>
  <div class="divider"></div>
  <div class="website">www.Marlowfamilyeyecare.example</div>

  <div class="band">
    <div class="band__cap"></div>
    <div class="band__main"><span class="address">4170 S Brackenridge Rd Wenatchee, WA 98802</span></div>
    <div class="band__cap"></div>
  </div>
</section>

<section class="card card--back">
  <div class="band band--top">
    <div class="band__cap"></div>
    <div class="band__main"><span class="band__title">NEXT APPOINTMENT</span></div>
    <div class="band__cap"></div>
  </div>

  <div class="field-line field-line--for"></div>
  <div class="field-label" style="top:128px;left:318px;">FOR</div>

  <div class="days">
    <span class="day">MON <span class="day__box"></span></span>
    <span class="day">TUE <span class="day__box"></span></span>
    <span class="day">WED <span class="day__box"></span></span>
    <span class="day">THUR <span class="day__box"></span></span>
    <span class="day">FRI <span class="day__box"></span></span>
    <span class="day">SAT <span class="day__box"></span></span>
  </div>

  <div class="field-line field-line--when"></div>
  <div class="field-label" style="top:267px;left:231px;">DATE</div>
  <div class="field-label" style="top:267px;left:397px;">TIME</div>

  <div class="policy">
    <div class="policy__title">CANCELLING POLICY</div>
    <div class="policy__text">If you are unable to keep your appointment , please allow 24 hours notice</div>
  </div>

  <div class="band band--bottom">
    <div class="band__cap"></div>
    <div class="band__main"></div>
    <div class="band__cap"></div>
  </div>
</section>

</body>
</html>
```